brisvole For High end Builder/developer construction

We will be a residential building company focused on a meticulous approach to high end quality builds with a design collaborative approach with all our clients to push the boundaries on new forms, products and bespoke architectural designs.

We want to be known to thrives upon collaboration with architects, designers and our clients to help them transform big ideas into inspiring spaces. We run every part of the building process, from planning through to construction and completion, is detail-focused and seamlessly managed.

Target Market(s)

High end

Font styles to use
Other font styles liked:
• Gotham Light

Colors

Designer to choose only greyscale colors for use in the design.

Requirements
Must have
• Bold headed incorporating sharp features for the logo to standout in mostly black to ensure the logo pops

```html
<!DOCTYPE html>
<html lang="en">
<head>
<meta charset="utf-8">
<title>Brisvole Letterhead</title>
<link href="https://fonts.googleapis.com/css2?family=Montserrat:wght@500&family=Open+Sans:wght@400&family=Roboto:wght@400&display=swap" rel="stylesheet">
<style>
:root{
  --backdrop:#e0e0e0;
  --ink:#0d0d0f;
  --accent:#8c8c8e;
  --accent-soft:#b4b4b6;
  --paper:#fafafa;
  --paper-alt:#ffffff;
  --body-text:#555558;
  --address-text:#3a3a3c;
  --company-text:#6e6e70;
  --white:#ffffff;
  --mark-grey:#efefef;
}
*{margin:0;padding:0;box-sizing:border-box}
html,body{width:1200px;height:800px;overflow:hidden;background:var(--backdrop)}
.letterhead{position:absolute;top:111px;width:411px;height:574px;background:var(--paper);overflow:hidden}
.letterhead--left{left:165px}
.letterhead--right{left:613px;width:407px;background:var(--paper-alt)}
.header{position:absolute;left:0;top:0;right:0;height:77px;background:var(--ink)}
.header-rule{position:absolute;left:0;right:0;top:78px;height:3px;background:var(--accent)}
.brand{position:absolute;left:36px;top:30px;display:flex;align-items:center;gap:6px;
  font-family:'Montserrat',sans-serif;font-weight:500;font-size:13px;letter-spacing:3px;color:var(--white)}
.brand-square{width:10px;height:10px;background:var(--accent-soft)}
.contact{position:absolute;left:282px;top:22px;list-style:none;font-family:'Roboto',sans-serif;font-size:7.6px;line-height:9.7px;color:var(--white)}
.letterhead--right .contact{left:280px}
.contact li{display:flex;align-items:center;gap:3px}
.contact svg{width:7px;height:7px;fill:var(--accent-soft)}
.letter{position:absolute;left:37px;top:146px;width:337px;font-family:'Open Sans',sans-serif;font-size:7.6px;line-height:11.1px;color:var(--body-text)}
.letter p{margin-bottom:11px;text-align:justify}
.letter .salutation{text-align:left}
.signature{position:absolute;left:37px;top:435px;width:48px;height:46px;background:linear-gradient(135deg,#ececec,#dcdcdc);opacity:.6}
.backdrop-mark{position:absolute;right:18px;bottom:17px;width:98px;height:98px;background:var(--mark-grey)}
.sender{position:absolute;left:37px;top:523px;font-family:'Roboto',sans-serif;font-size:8.6px;line-height:10.2px;color:var(--address-text);font-style:normal}
.sender .company{color:var(--company-text)}
.footer-rule{position:absolute;left:0;right:0;bottom:15px;height:3px;background:var(--accent)}
.footer-band{position:absolute;left:0;right:0;bottom:0;height:12px;background:var(--ink)}
</style>
</head>
<body>

<article class="letterhead letterhead--left">
  <header class="header">
    <div class="brand"><span class="brand-square"></span>BRISVOLE</div>
    <ul class="contact">
      <li><svg viewBox="0 0 10 10"><path d="M1 3c2-2 6-2 8 0v2H7V4H3v1H1z M2 6h6v3H2z"/></svg>555.204.1180</li>
      <li><svg viewBox="0 0 10 10"><rect x="3" y="1" width="4" height="3"/><rect x="1" y="4" width="8" height="4"/><rect x="3" y="7" width="4" height="2"/></svg>555.204.1190</li>
      <li><svg viewBox="0 0 10 10"><path d="M1 2h8v6H1z"/></svg>mara@brisvole.example</li>
      <li><svg viewBox="0 0 10 10"><circle cx="5" cy="5" r="4"/></svg>www.brisvole.example</li>
    </ul>
  </header>
  <div class="header-rule"></div>
  <div class="backdrop-mark" aria-hidden="true"></div>
  <section class="letter">
    <p class="salutation">Dear customer,</p>
    <p>Lorem ipsum dolor sit amet, consectetur adipisicing elit, sed do eiusmod tempor incididunt ut labore et dolore magna aliqua. Ut enim ad minim veniam, quis nostrud exercitation ullamco laboris nisi ut aliquip ex ea commodo consequat. Duis aute irure dolor in reprehenderit in voluptate velit esse cillum dolore eu fugiat nulla pariatur. Excepteur sint occaecat cupidatat non proident, sunt in culpa qui officia deserunt mollit anim id est laborum.</p>
    <p>Lorem ipsum dolor sit amet, consectetur adipisicing elit, sed do eiusmod tempor incididunt ut labore et dolore magna aliqua. Ut enim ad minim veniam, quis nostrud exercitation ullamco laboris nisi ut aliquip ex ea commodo consequat. Duis aute irure dolor in reprehenderit in voluptate velit esse cillum dolore eu fugiat nulla pariatur. Excepteur sint occaecat cupidatat non proident, sunt in culpa qui officia deserunt mollit anim id est laborum.</p>
    <p>Lorem ipsum dolor sit amet, consectetur adipisicing elit, sed do eiusmod tempor incididunt ut labore et dolore magna aliqua. Ut enim ad minim veniam, quis nostrud exercitation ullamco laboris nisi ut aliquip ex ea commodo consequat. Duis aute irure dolor in reprehenderit in voluptate velit esse cillum dolore eu fugiat nulla pariatur. Excepteur sint occaecat cupidatat non proident, sunt in culpa qui officia deserunt mollit anim id est laborum.</p>
    <p>Lorem ipsum dolor sit amet, consectetur adipisicing elit, sed do eiusmod tempor incididunt ut labore et dolore magna aliqua. Ut enim ad minim veniam, quis nostrud exercitation ullamco laboris nisi ut aliquip ex ea commodo consequat. Duis aute irure dolor in reprehenderit.</p>
    <p class="salutation">Yours Sincerely,</p>
  </section>
  <div class="signature" role="img" aria-label="Handwritten signature"></div>
  <address class="sender">
    <div class="company">Brisvole Building Studio</div>
    <div>4/62 Harbour Lane</div>
    <div>Elmford NSW 2999</div>
  </address>
  <div class="footer-rule"></div>
  <div class="footer-band"></div>
</article>

<article class="letterhead letterhead--right">
  <header class="header">
    <div class="brand"><span class="brand-square"></span>BRISVOLE</div>
    <ul class="contact">
      <li><svg viewBox="0 0 10 10"><path d="M1 3c2-2 6-2 8 0v2H7V4H3v1H1z M2 6h6v3H2z"/></svg>555.204.1180</li>
      <li><svg viewBox="0 0 10 10"><rect x="3" y="1" width="4" height="3"/><rect x="1" y="4" width="8" height="4"/><rect x="3" y="7" width="4" height="2"/></svg>555.204.1190</li>
      <li><svg viewBox="0 0 10 10"><path d="M1 2h8v6H1z"/></svg>mara@brisvole.example</li>
      <li><svg viewBox="0 0 10 10"><circle cx="5" cy="5" r="4"/></svg>www.brisvole.example</li>
    </ul>
  </header>
  <div class="header-rule"></div>
  <div class="backdrop-mark" aria-hidden="true"></div>
  <section class="letter">
    <p class="salutation">Dear customer,</p>
    <p>Lorem ipsum dolor sit amet, consectetur adipisicing elit, sed do eiusmod tempor incididunt ut labore et dolore magna aliqua. Ut enim ad minim veniam, quis nostrud exercitation ullamco laboris nisi ut aliquip ex ea commodo consequat. Duis aute irure dolor in reprehenderit in voluptate velit esse cillum dolore eu fugiat nulla pariatur. Excepteur sint occaecat cupidatat non proident, sunt in culpa qui officia deserunt mollit anim id est laborum.</p>
    <p>Lorem ipsum dolor sit amet, consectetur adipisicing elit, sed do eiusmod tempor incididunt ut labore et dolore magna aliqua. Ut enim ad minim veniam, quis nostrud exercitation ullamco laboris nisi ut aliquip ex ea commodo consequat. Duis aute irure dolor in reprehenderit in voluptate velit esse cillum dolore eu fugiat nulla pariatur. Excepteur sint occaecat cupidatat non proident, sunt in culpa qui officia deserunt mollit anim id est laborum.</p>
    <p>Lorem ipsum dolor sit amet, consectetur adipisicing elit, sed do eiusmod tempor incididunt ut labore et dolore magna aliqua. Ut enim ad minim veniam, quis nostrud exercitation ullamco laboris nisi ut aliquip ex ea commodo consequat. Duis aute irure dolor in reprehenderit in voluptate velit esse cillum dolore eu fugiat nulla pariatur. Excepteur sint occaecat cupidatat non proident, sunt in culpa qui officia deserunt mollit anim id est laborum.</p>
    <p>Lorem ipsum dolor sit amet, consectetur adipisicing elit, sed do eiusmod tempor incididunt ut labore et dolore magna aliqua. Ut enim ad minim veniam, quis nostrud exercitation ullamco laboris nisi ut aliquip ex ea commodo consequat. Duis aute irure dolor in reprehenderit.</p>
    <p class="salutation">Yours Sincerely,</p>
  </section>
  <div class="signature" role="img" aria-label="Handwritten signature"></div>
  <address class="sender">
    <div class="company">Brisvole Building Studio</div>
    <div>4/62 Harbour Lane</div>
    <div>Elmford NSW 2999</div>
  </address>
  <div class="footer-rule"></div>
  <div class="footer-band"></div>
</article>

</body>
</html>
```